Design the Mobile Version of Existing Web Based Health Platform

Nuvorel is a social business enterprise that focus on public health by applying innovative healthcare services and consumer internet technology. Nuvorel offers a personalized platform of health promotion and disease prevention that puts the individual back in control of his life.

Nuvorel is looking for a Mobile Web UX/Visual Design professional to create a mobile version of Nuvorel website platform for iPhone, iPad/tablet and Android.

Contestants must to check www.nuvorel-saude.com.br to have a better understanding of Nuvorel Platform by creating an account (it's in portuguese, but anyone can get the general idea).

The mobile version of Nuvorel should have very similar functionality and user flows. This job is not to reengineer or re-imagine Nuvorel. It is just to reformat the existing functionality so it works well on mobile devices.

This description below is to help you to understand the core features of the platform (check the attachments to see the new web design of each one):

- Personally Controlled Health Record - PCHR enables an individual to own and manage a complete, secure, digital copy of her health and wellness information.
- Health Risk Assessments - is a process to estimate the nature and probability of adverse health effects, based on personal and family historical data, behavior and environment.
- Simulation of future health - "what if analysis" that emphasizes health education and behavior change.
- Daily Challenges - a program that gives you the opportunity to the participant to advance his personal well-being by doing simple daily challenges
- Health Alerts and Recommendations and Missing Data - Recommendations based on Health Ministry Guidelines and National Wellness Review Board (NWRB), plus notifications to update outdated information.

The deliverable for this project is a psd file with a designed mobile version of Nuvorel.

A new design of the web platform is under construction. You can also check it looking at the files attached.

Target Market(s)

people 25-40 years old, 60% female, socially engaged

Industry/Entity Type

Healthcare

Requirements
Must have
• iPhone, iPad and Android version

Design must cover all current functionalities available on the web version (please, ensure you understand all features by creating an account at www.nuvorel-saude.com.br)

- Login/Sign up
- Welcome (first assessment)
- Add to Personal Controlled Health Record (PCHR)
- Update/Remove PCHR
- List PCHR
- Bodyscope (risk assessmen results)
- Simulation
- Alerts
- Missing data
- Recommendations
- StepQuest
- Badges
- Configurations

It's important to check the attachments to see how the web platform design is evolving.

```html
<!DOCTYPE html>
<html lang="en">
<head>
<meta charset="utf-8">
<title>Nuvorel – Simulation</title>
<link href="https://fonts.googleapis.com/css2?family=Arimo:wght@400;700&display=swap" rel="stylesheet">
<style>
  :root{
    --orange:#f7923a;
    --orange-dark:#f07a2a;
    --green:#99cc33;
    --grey-tab:#a8a8a8;
    --grey-icon:#6d6d6d;
    --grey-label:#555;
    --grey-hint:#9a9a9a;
    --border:#d7d7d7;
    --page:#f4f4f4;
    --ink:#333;
    --red:#ee1c24;
    --amber:#ffa500;
    --yellow:#ffd700;
    --lime:#9acd32;
    --olive:#5b8c1e;
  }
  html,body{margin:0;padding:0;width:799px;height:1200px;overflow:hidden;background:var(--page);}
  body{font-family:"Arimo",Arial,sans-serif;}
  .screen{position:relative;width:640px;height:960px;transform:scale(1.2484,1.25);transform-origin:0 0;background:var(--page);overflow:hidden;}
  .abs{position:absolute;}

  .topbar{left:0;top:0;width:640px;height:70px;background:#fff;border-bottom:1px solid #e2e2e2;}
  .avatar{left:8px;top:8px;width:62px;height:60px;background:linear-gradient(160deg,#8a8f94,#4d4a45 60%,#a89a80);}
  .divider{top:0;width:1px;height:70px;background:#dcdcdc;}
  .brand{left:100px;top:0;width:468px;height:70px;display:flex;align-items:center;justify-content:center;}
  .brand-name{font-size:34px;font-weight:700;color:var(--ink);line-height:1;}
  .menu{left:587px;top:20px;width:36px;}
  .menu span{display:block;height:7px;border-radius:4px;background:#5a5a5a;margin-bottom:5px;}

  .recordbar{left:0;top:71px;width:640px;height:59px;background:linear-gradient(#fbae6c,var(--orange-dark));}
  .record-input{left:106px;top:18px;width:364px;height:26px;background:#fff;border:1px solid #e6e6e6;font-size:12px;color:var(--grey-hint);line-height:26px;padding-left:18px;box-sizing:border-box;}
  .partner{left:483px;top:13px;display:flex;align-items:center;gap:5px;color:#fff;font-size:13px;font-weight:700;line-height:15px;}
  .partner-dot{width:26px;height:26px;border-radius:50%;background:#fff;opacity:.9;}

  .tab{top:141px;height:29px;line-height:29px;text-align:center;color:#fff;font-size:14px;font-weight:700;}
  .tab-active{left:203px;width:159px;background:var(--green);}
  .tab-idle{left:363px;width:155px;background:var(--grey-tab);}

  .body-map{left:40px;top:180px;width:146px;height:520px;border-radius:60px 60px 20px 20px;background:radial-gradient(circle at 50% 22%,#ffd2ac,#fbe7d6 55%,#f6efe8);}

  .field-label{font-size:14px;font-weight:700;color:var(--grey-label);}
  .field-icon{width:30px;height:30px;}
  .field-input{height:31px;background:#fff;border:1px solid var(--border);box-sizing:border-box;font-size:12px;color:var(--grey-hint);text-align:right;line-height:29px;padding-right:10px;}
  .spinner{width:16px;height:31px;background:#fff;border:1px solid var(--border);box-sizing:border-box;border-radius:3px;font-size:8px;color:#666;text-align:center;line-height:13px;}

  .btn{top:661px;width:125px;height:32px;background:var(--orange);color:#fff;font-size:13px;font-weight:700;text-align:center;line-height:32px;border:1px solid var(--orange-dark);box-sizing:border-box;}

  .legend{left:25px;top:717px;font-size:12px;color:var(--grey-hint);}
  .legend li{list-style:none;height:23.5px;display:flex;align-items:center;gap:8px;}
  .legend ul{margin:0;padding:0;}
  .legend i{width:13px;height:13px;border-radius:50%;display:inline-block;}

  .risk{left:193px;height:30px;display:flex;align-items:center;gap:15px;font-size:15px;font-weight:700;color:var(--ink);}
  .risk-tag{width:19px;height:30px;background:var(--grey-icon);border-radius:4px 0 0 4px;}

  .tabbar{left:0;top:895px;width:640px;height:65px;background:linear-gradient(#fafafa,#e8e8e8);border-top:1px solid #cfcfcf;}
  .nav-icon{top:12px;width:40px;height:40px;}
  .badge{left:205px;top:32px;width:21px;height:21px;border-radius:50%;background:var(--orange);color:#fff;font-size:11px;font-weight:700;text-align:center;line-height:21px;}
</style>
</head>
<body>
<div class="screen">

  <header class="abs topbar">
    <div class="abs avatar" role="img" aria-label="User profile photo"></div>
    <svg class="abs" style="left:76px;top:33px" width="20" height="14" viewBox="0 0 20 14"><path d="M2 2 L10 10 L18 2" stroke="#555" stroke-width="4" fill="none"/></svg>
    <div class="abs divider" style="left:100px"></div>
    <div class="abs brand"><div class="brand-name">Nuvorel</div></div>
    <div class="abs divider" style="left:568px"></div>
    <div class="abs menu"><span></span><span></span><span></span></div>
  </header>

  <section class="abs recordbar">
    <svg class="abs" style="left:75px;top:13px" width="26" height="34" viewBox="0 0 26 34"><rect x="1" y="4" width="24" height="29" rx="3" fill="#fff"/><rect x="8" y="1" width="10" height="6" rx="2" fill="#fff" stroke="#f4853a"/><g stroke="#f4853a" stroke-width="2"><line x1="6" y1="13" x2="20" y2="13"/><line x1="6" y1="18" x2="20" y2="18"/><line x1="6" y1="23" x2="20" y2="23"/><line x1="6" y1="28" x2="20" y2="28"/></g></svg>
    <div class="abs record-input">Add a new record</div>
    <div class="abs partner"><div class="partner-dot"></div><div>Calderin<br>Pharma</div></div>
  </section>

  <div class="abs tab tab-active">Simulation</div>
  <div class="abs tab tab-idle">My goal</div>

  <div class="abs body-map" role="img" aria-label="Body outline with highlighted risk areas on head, chest, abdomen and hip"></div>

  <svg class="abs field-icon" style="left:204px;top:186px" viewBox="0 0 30 30"><rect x="2" y="2" width="26" height="26" rx="4" fill="var(--grey-icon)"/><circle cx="15" cy="11" r="6" fill="#fff"/><line x1="15" y1="11" x2="18" y2="8" stroke="var(--grey-icon)" stroke-width="2"/></svg>
  <div class="abs field-label" style="left:243px;top:205px">Height</div>
  <div class="abs field-input" style="left:203px;top:231px;width:148px">Kg</div>
  <div class="abs spinner" style="left:357px;top:231px">▲<br>▼</div>

  <svg class="abs field-icon" style="left:204px;top:282px" viewBox="0 0 30 30"><rect x="2" y="17" width="22" height="7" fill="var(--grey-icon)"/><rect x="25" y="17" width="3" height="7" fill="var(--grey-icon)"/><path d="M22 4 q4 5 0 10 M26 4 q4 5 0 10" stroke="var(--grey-icon)" stroke-width="2" fill="none"/></svg>
  <div class="abs field-label" style="left:243px;top:299px">Cigarettes</div>
  <div class="abs field-input" style="left:203px;top:321px;width:148px">/day</div>
  <div class="abs spinner" style="left:357px;top:321px">▲<br>▼</div>

  <svg class="abs field-icon" style="left:204px;top:368px" viewBox="0 0 30 30"><rect x="6" y="2" width="8" height="18" rx="4" fill="var(--grey-icon)" transform="rotate(-35 10 11)"/><path d="M20 12 q6 8 0 14 q-6 -6 0 -14z" fill="var(--grey-icon)"/></svg>
  <div class="abs field-label" style="left:243px;top:389px">Good cholesterol</div>
  <div class="abs field-input" style="left:203px;top:410px;width:148px">mg/dl</div>
  <div class="abs spinner" style="left:357px;top:410px">▲<br>▼</div>

  <svg class="abs field-icon" style="left:204px;top:464px" viewBox="0 0 30 30"><circle cx="15" cy="6" r="4" fill="var(--grey-icon)"/><rect x="9" y="11" width="12" height="10" rx="2" fill="var(--grey-icon)"/><rect x="1" y="23" width="28" height="6" fill="none" stroke="var(--grey-icon)" stroke-width="2"/></svg>
  <div class="abs field-label" style="left:243px;top:488px">Waist</div>
  <div class="abs field-input" style="left:200px;top:511px;width:148px">cm</div>
  <div class="abs spinner" style="left:355px;top:511px">▲<br>▼</div>

  <svg class="abs field-icon" style="left:204px;top:564px" viewBox="0 0 30 30"><circle cx="19" cy="11" r="9" fill="none" stroke="var(--grey-icon)" stroke-width="3"/><line x1="19" y1="11" x2="23" y2="7" stroke="var(--grey-icon)" stroke-width="2"/><ellipse cx="7" cy="24" rx="6" ry="5" fill="var(--grey-icon)"/></svg>
  <div class="abs field-label" style="left:243px;top:586px">Pressure</div>
  <div class="abs field-input" style="left:200px;top:608px;width:148px">mmhg</div>
  <div class="abs spinner" style="left:355px;top:608px">▲<br>▼</div>

  <svg class="abs field-icon" style="left:428px;top:186px" viewBox="0 0 30 30"><path d="M6 20 q0 -14 10 -16 l4 4 l-6 2 q-2 4 2 6 q8 -2 10 6 q-4 6 -20 -2z" fill="var(--grey-icon)"/><path d="M1 26 h6 l2 -3 l2 5 l2 -3 h16" stroke="var(--grey-icon)" fill="none"/></svg>
  <div class="abs field-label" style="left:467px;top:205px">Physical activity</div>
  <div class="abs field-input" style="left:425px;top:231px;width:148px">/ week</div>
  <div class="abs spinner" style="left:582px;top:231px">▲<br>▼</div>

  <svg class="abs field-icon" style="left:423px;top:280px" viewBox="0 0 30 30"><path d="M15 2 q11 14 0 26 q-11 -12 0 -26z" fill="var(--grey-icon)"/></svg>
  <div class="abs field-label" style="left:461px;top:299px">Total cholesterol</div>
  <div class="abs field-input" style="left:425px;top:321px;width:148px">mg/dl</div>
  <div class="abs spinner" style="left:582px;top:321px">▲<br>▼</div>

  <svg class="abs field-icon" style="left:423px;top:368px" viewBox="0 0 30 30"><rect x="4" y="2" width="20" height="20" rx="3" fill="var(--grey-icon)"/><rect x="7" y="8" width="14" height="10" fill="#fff"/><line x1="14" y1="22" x2="14" y2="29" stroke="var(--grey-icon)" stroke-width="2"/></svg>
  <div class="abs field-label" style="left:458px;top:389px">Glucose</div>
  <div class="abs field-input" style="left:423px;top:410px;width:148px">mg/dl</div>
  <div class="abs spinner" style="left:582px;top:410px">▲<br>▼</div>

  <svg class="abs field-icon" style="left:421px;top:466px" viewBox="0 0 30 30"><rect x="14" y="1" width="2" height="10" fill="var(--grey-icon)"/><path d="M13 10 q-10 -2 -12 12 q0 6 6 4 q6 -2 6 -12z M17 10 q10 -2 12 12 q0 6 -6 4 q-6 -2 -6 -12z" fill="var(--grey-icon)"/></svg>
  <div class="abs field-label" style="left:460px;top:488px">Breathing</div>
  <div class="abs field-input" style="left:423px;top:511px;width:148px">mg/dl</div>
  <div class="abs spinner" style="left:582px;top:511px">▲<br>▼</div>

  <div class="abs btn" style="left:187px">calculate</div>
  <div class="abs btn" style="left:331px">set target</div>
  <div class="abs btn" style="left:473px">clean</div>

  <div class="abs legend">
    <ul>
      <li><i style="background:var(--orange)"></i>Condição pré-existente</li>
      <li><i style="background:var(--red)"></i>Alto</li>
      <li><i style="background:var(--amber)"></i>Acima da Média</li>
      <li><i style="background:var(--yellow)"></i>Na Média</li>
      <li><i style="background:var(--lime)"></i>Abaixo da Média</li>
      <li><i style="background:var(--olive)"></i>Baixo</li>
    </ul>
  </div>

  <div class="abs risk" style="top:714px"><span class="risk-tag"></span>Risco de arterial coronariana : 0,15%</div>
  <div class="abs risk" style="top:752px"><span class="risk-tag"></span>Risco de derrame cerebral : 0,25%</div>
  <div class="abs risk" style="top:789px"><span class="risk-tag"></span>Risco de cancer : 0,13%</div>
  <div class="abs risk" style="top:826px"><span class="risk-tag"></span>Risco de diabetes : 0,20%</div>

  <nav class="abs tabbar">
    <svg class="abs nav-icon" style="left:58px" viewBox="0 0 40 40" fill="#b5b5b5"><rect x="2" y="6" width="10" height="10"/><rect x="14" y="4" width="10" height="10"/><rect x="26" y="2" width="11" height="11"/><rect x="2" y="18" width="10" height="10"/><rect x="14" y="16" width="10" height="10"/><rect x="26" y="15" width="11" height="11"/><rect x="2" y="30" width="10" height="8"/><rect x="14" y="28" width="10" height="10"/></svg>
    <svg class="abs nav-icon" style="left:176px" viewBox="0 0 40 40"><path d="M20 3 L38 36 H2z" fill="#b5b5b5"/><rect x="18" y="14" width="4" height="12" fill="#fff"/><rect x="18" y="29" width="4" height="4" fill="#fff"/></svg>
    <div class="abs badge">15</div>
    <svg class="abs nav-icon" style="left:298px" viewBox="0 0 40 40"><rect x="2" y="12" width="36" height="24" fill="#b5b5b5"/><path d="M2 12 L20 26 L38 12" stroke="#fff" stroke-width="2" fill="none"/><rect x="9" y="3" width="22" height="14" fill="#ccc" stroke="#fff"/></svg>
    <svg class="abs nav-icon" style="left:416px" viewBox="0 0 40 40"><ellipse cx="20" cy="18" rx="18" ry="13" fill="#b5b5b5"/><path d="M10 27 L6 37 L18 30z" fill="#b5b5b5"/><circle cx="12" cy="18" r="2.5" fill="#fff"/><circle cx="20" cy="18" r="2.5" fill="#fff"/><circle cx="28" cy="18" r="2.5" fill="#fff"/></svg>
    <svg class="abs nav-icon" style="left:538px" viewBox="0 0 40 40"><circle cx="20" cy="20" r="18" fill="#b5b5b5"/><text x="20" y="28" text-anchor="middle" font-family="Arimo,Arial,sans-serif" font-weight="700" font-size="22" fill="#fff">?</text></svg>
  </nav>

</div>
</body>
</html>
```